Quarrow financial services, is a financial company that provides consultancy, brokerage services, and funding.

we will be providing the clients with insights, knowledge and data with regards to the financial markets.

with the brokerage services we will try to find the suitable counterparts that provide them with the best investments that suits their needs and expected return.

Target Market(s)

financial institutions, Corporates, high-net worth individuals

Industry/Entity Type

Financial Service

Contact Information for Business Card

Font styles to use
Other font styles liked:
• applemyungjo

Colors
00a990
848484

Requirements
Must have
• the logo at the back
Nice to have
• Finesse
Should not have
• boldness

```html
<!DOCTYPE html>
<html lang="en">
<head>
<meta charset="utf-8">
<title>Quarrow Financial Services – Business Card</title>
<link href="https://fonts.googleapis.com/css2?family=Cinzel:wght@400&family=Libre+Baskerville&family=Roboto:wght@400&display=swap" rel="stylesheet">
<style>
  :root {
    --backdrop: #e6e6e6;
    --card: #ffffff;
    --ink: #3a4448;
    --teal: #2e8a78;
    --grey: #5e5e5e;
    --sage: #b9cba6;
  }
  * { box-sizing: border-box; margin: 0; padding: 0; }
  html, body { width: 1200px; height: 443px; overflow: hidden; background: var(--backdrop); }
  .canvas { position: relative; width: 1200px; height: 443px; }
  .card {
    position: absolute; top: 72px; width: 484px; height: 294px;
    background: var(--card); border-radius: 16px;
  }
  .card--front { left: 82px; }
  .card--back { left: 602px; }

  /* front */
  .brand-block {
    position: absolute; left: 0; right: 0; top: 60px;
    display: flex; flex-direction: column; align-items: center;
  }
  .brand-square { width: 70px; height: 70px; background: var(--sage); margin-bottom: 38px; }
  .brand-name {
    font-family: "Cinzel", serif; font-weight: 400; font-size: 36px;
    letter-spacing: 2px; color: var(--ink); line-height: 1;
  }
  .brand-sub {
    font-family: "Cinzel", serif; font-size: 12px; letter-spacing: 2.6px;
    color: var(--ink); margin-top: 5px;
  }
  .brand-tagline {
    font-family: "Cinzel", serif; font-size: 10px; letter-spacing: 0.6px;
    color: var(--ink); margin-top: 4px;
  }

  /* back */
  .back-mark {
    position: absolute; left: 88px; top: 98px;
    display: flex; flex-direction: column; align-items: center;
  }
  .back-mark .brand-square { width: 60px; height: 60px; margin-bottom: 10px; }
  .back-mark .brand-name { font-size: 15px; letter-spacing: 1px; }

  .contact { position: absolute; left: 231px; top: 78px; }
  .person-name {
    font-family: "Libre Baskerville", serif; font-size: 19px; color: var(--teal);
  }
  .person-role {
    font-family: "Roboto", sans-serif; font-size: 11px; color: var(--grey);
    margin-top: 4px; margin-bottom: 8px;
  }
  .contact-list { list-style: none; }
  .contact-list li, .address {
    font-family: "Libre Baskerville", serif; font-size: 11.5px; color: var(--grey);
    line-height: 18px;
  }
  .contact-list li { display: flex; align-items: center; gap: 10px; }
  .contact-list svg { width: 11px; height: 11px; fill: var(--teal); flex: none; }
  .address { margin-top: 8px; line-height: 20px; }
</style>
</head>
<body>
<div class="canvas">
  <section class="card card--front">
    <div class="brand-block">
      <div class="brand-square"></div>
      <div class="brand-name">QUARROW</div>
      <div class="brand-sub">FINANCIAL SERVICES</div>
      <div class="brand-tagline">YOUR FINANCIAL FUTURE IS OUR PRIORITY</div>
    </div>
  </section>

  <section class="card card--back">
    <div class="back-mark">
      <div class="brand-square"></div>
      <div class="brand-name">QUARROW</div>
    </div>
    <div class="contact">
      <div class="person-name">Daniel Hart</div>
      <div class="person-role">Managing Director</div>
      <ul class="contact-list">
        <li><svg viewBox="0 0 12 12"><path d="M1 4c0-2 2-3 5-3s5 1 5 3v1H8V3.5H4V5H1z M3 6h6l2 5H1z"/></svg>00-214-555-0147</li>
        <li><svg viewBox="0 0 12 12"><circle cx="6" cy="6" r="5.2" fill="none" stroke="#2e8a78" stroke-width="1.2"/><path d="M6 .8v10.4M.8 6h10.4" stroke="#2e8a78" stroke-width="1"/><ellipse cx="6" cy="6" rx="2.3" ry="5.2" fill="none" stroke="#2e8a78" stroke-width="1"/></svg>www.quarrowfinance.com</li>
        <li><svg viewBox="0 0 12 12"><path d="M0 2h12v8H0z"/><path d="M0 2l6 5 6-5" fill="none" stroke="#fff" stroke-width="1"/></svg>daniel@quarrowfinance.com</li>
      </ul>
      <div class="address">4215 Maple Hollow Road<br>Glendale California 91205</div>
    </div>
  </section>
</div>
</body>
</html>
```